Spinning Wheel: Spin & Win

We are looking to design a large sticker cover for a spinning wheel (please see attached reference)

Wheel diameter: 120 cm (1.2meters)

Divided into 8 sections:
1- Free Meal
2- Talvor Gift Card
3- Haircut or Blowdry
4- Talvor Gift Card
5- Merchandise
6- Talvor Gift Card
7- Meal voucher
8- Talvor Gift Card

Text in the center:
Buy for 200 AED to Spin & Win!
(Spin & Win should be the most dominant visually)

Font: Something classy and elegant (maybe cursive but easily read)

Colors: Khaki - All shades of brown and dark brown (note: the wheel structure is made of wood that is dark brown)

Feel: Wood and Old Paper

Target Market(s)

Upper Class

Industry/Entity Type

Graphic Design

Font styles to use
Decorative
Script

Requirements
Should not have
• Flashy colors

```html
<!DOCTYPE html>
<html lang="en">
<head>
<meta charset="utf-8">
<title>Spin &amp; Win Wheel Cover</title>
<link rel="stylesheet" href="https://fonts.googleapis.com/css2?family=Almendra:wght@400;700&family=Berkshire+Swash&family=Oswald:wght@400&display=swap">
<style>
  :root {
    --page: #ffffff;
    --paper-light: #f9d386;
    --paper-light-edge: #e9a94c;
    --paper-deep: #f1bc65;
    --paper-deep-edge: #dc8f34;
    --rim: #c97a2a;
    --label: #b23a17;
    --ornament: #dcae6a;
    --medallion-core: #a4552a;
    --medallion-edge: #5e2710;
    --medallion-rim: #e7b86a;
    --gold-text: #f7d889;
  }
  html, body {
    margin: 0;
    padding: 0;
    width: 1200px;
    height: 1200px;
    overflow: hidden;
    background: var(--page);
  }
  .wheel-canvas {
    display: block;
    width: 1200px;
    height: 1200px;
  }
  .sector-label {
    font-family: "Almendra", serif;
    font-weight: 700;
    font-size: 44px;
    fill: var(--label);
  }
  .hub-lead {
    font-family: "Oswald", sans-serif;
    font-size: 32px;
    fill: var(--gold-text);
  }
  .hub-title {
    font-family: "Berkshire Swash", cursive;
    fill: var(--gold-text);
  }
  .hub-title--word { font-size: 104px; }
  .hub-title--amp { font-size: 40px; }
</style>
</head>
<body>
<svg class="wheel-canvas" viewBox="0 0 1200 1200" xmlns="http://www.w3.org/2000/svg">
  <defs>
    <radialGradient id="sector-light" cx="600" cy="600" r="588" gradientUnits="userSpaceOnUse">
      <stop offset="0.3" stop-color="var(--paper-light)"/>
      <stop offset="1" stop-color="var(--paper-light-edge)"/>
    </radialGradient>
    <radialGradient id="sector-deep" cx="600" cy="600" r="588" gradientUnits="userSpaceOnUse">
      <stop offset="0.3" stop-color="var(--paper-deep)"/>
      <stop offset="1" stop-color="var(--paper-deep-edge)"/>
    </radialGradient>
    <radialGradient id="hub-ornament" cx="0.5" cy="0.5" r="0.5">
      <stop offset="0.6" stop-color="#c98a45"/>
      <stop offset="1" stop-color="#e8c487" stop-opacity="0.6"/>
    </radialGradient>
    <radialGradient id="medallion" cx="0.45" cy="0.4" r="0.6">
      <stop offset="0" stop-color="var(--medallion-core)"/>
      <stop offset="1" stop-color="var(--medallion-edge)"/>
    </radialGradient>
    <path id="wedge" d="M0 0 L-225 -543.2 A588 588 0 0 1 225 -543.2 Z"/>
  </defs>

  <g class="wheel-sectors" transform="translate(600 600)">
    <use href="#wedge" fill="url(#sector-deep)" transform="rotate(0)"/>
    <use href="#wedge" fill="url(#sector-light)" transform="rotate(45)"/>
    <use href="#wedge" fill="url(#sector-deep)" transform="rotate(90)"/>
    <use href="#wedge" fill="url(#sector-light)" transform="rotate(135)"/>
    <use href="#wedge" fill="url(#sector-deep)" transform="rotate(180)"/>
    <use href="#wedge" fill="url(#sector-light)" transform="rotate(225)"/>
    <use href="#wedge" fill="url(#sector-deep)" transform="rotate(270)"/>
    <use href="#wedge" fill="url(#sector-light)" transform="rotate(315)"/>
  </g>

  <g class="rim-ornaments" role="img" aria-label="Gilded acanthus scroll ornaments along the rim of each sector" transform="translate(600 600)">
    <ellipse cx="0" cy="-530" rx="120" ry="40" fill="var(--ornament)" opacity="0.75" transform="rotate(0)"/>
    <ellipse cx="0" cy="-530" rx="120" ry="40" fill="var(--ornament)" opacity="0.75" transform="rotate(45)"/>
    <ellipse cx="0" cy="-530" rx="120" ry="40" fill="var(--ornament)" opacity="0.75" transform="rotate(90)"/>
    <ellipse cx="0" cy="-530" rx="120" ry="40" fill="var(--ornament)" opacity="0.75" transform="rotate(135)"/>
    <ellipse cx="0" cy="-530" rx="120" ry="40" fill="var(--ornament)" opacity="0.75" transform="rotate(180)"/>
    <ellipse cx="0" cy="-530" rx="120" ry="40" fill="var(--ornament)" opacity="0.75" transform="rotate(225)"/>
    <ellipse cx="0" cy="-530" rx="120" ry="40" fill="var(--ornament)" opacity="0.75" transform="rotate(270)"/>
    <ellipse cx="0" cy="-530" rx="120" ry="40" fill="var(--ornament)" opacity="0.75" transform="rotate(315)"/>
  </g>

  <circle class="wheel-rim" cx="600" cy="600" r="587" fill="none" stroke="var(--rim)" stroke-width="2"/>

  <g class="sector-labels" text-anchor="middle" dominant-baseline="central">
    <g transform="translate(600 600) rotate(0) translate(0 -368) rotate(90)">
      <text class="sector-label"><tspan x="0" y="-36">Free</tspan><tspan x="0" y="36">Meal</tspan></text>
    </g>
    <g transform="translate(600 600) rotate(45) translate(0 -355) rotate(90)">
      <text class="sector-label"><tspan x="0" y="-36">Talvor</tspan><tspan x="0" y="36">Gift Card</tspan></text>
    </g>
    <g transform="translate(600 600) rotate(90) translate(0 -368) rotate(90)">
      <text class="sector-label"><tspan x="0" y="-36">Haircut or</tspan><tspan x="0" y="36">Blowdry</tspan></text>
    </g>
    <g transform="translate(600 600) rotate(135) translate(0 -355) rotate(90)">
      <text class="sector-label"><tspan x="0" y="-36">Talvor</tspan><tspan x="0" y="36">Gift Card</tspan></text>
    </g>
    <g transform="translate(600 600) rotate(180) translate(0 -342) rotate(90)">
      <text class="sector-label" x="0" y="0" textLength="212" lengthAdjust="spacingAndGlyphs">Merchandise</text>
    </g>
    <g transform="translate(600 600) rotate(225) translate(0 -355) rotate(90)">
      <text class="sector-label"><tspan x="0" y="-36">Talvor</tspan><tspan x="0" y="36">Gift Card</tspan></text>
    </g>
    <g transform="translate(600 600) rotate(270) translate(0 -350) rotate(90)">
      <text class="sector-label"><tspan x="0" y="-36">Meal</tspan><tspan x="0" y="36">Voucher</tspan></text>
    </g>
    <g transform="translate(600 600) rotate(315) translate(0 -355) rotate(90)">
      <text class="sector-label"><tspan x="0" y="-36">Talvor</tspan><tspan x="0" y="36">Gift Card</tspan></text>
    </g>
  </g>

  <g class="hub">
    <circle class="hub-ornament" cx="600" cy="600" r="226" fill="url(#hub-ornament)" role="img" aria-label="Carved golden leaf sunburst framing the centre medallion"/>
    <circle class="hub-medallion" cx="600" cy="600" r="166" fill="url(#medallion)" stroke="var(--medallion-rim)" stroke-width="4"/>
    <text class="hub-lead" x="606" y="472" text-anchor="middle">Buy for</text>
    <text class="hub-lead" x="652" y="516" text-anchor="middle">200 AED to</text>
    <text class="hub-title hub-title--word" x="462" y="612" textLength="136" lengthAdjust="spacingAndGlyphs">Spin</text>
    <text class="hub-title hub-title--amp" x="612" y="626">&amp;</text>
    <text class="hub-title hub-title--word" x="562" y="730" textLength="140" lengthAdjust="spacingAndGlyphs">Win!</text>
  </g>
</svg>
</body>
</html>
```